Stationery Design
Letterhead, Envelope, Business Card, Email signature design
I need single sided standard sized Business Card [3.5" x 2"]
Myriad Pro
Professional
Corisse Pallant
Brand Manager
4127 Dunford Avenue
Burnaby, B.C. V3K 8T2
604-281-7734 ext. 120
corisse@brightfernco.ca
brightfernco.ca
We are a family-owned school photography company in Western Canada. We've just had a new logo and website designed and need some new stationery.
This is the .ai file we would like to use for the stationery design. Please refer to our website, brightfernco.ca, for more information about our brand.

```html
<!DOCTYPE html>
<html lang="en">
<head>
<meta charset="utf-8">
<title>Bright Fern Co. – Business Card – Corisse Pallant</title>
<link rel="stylesheet" href="https://fonts.googleapis.com/css2?family=PT+Sans:wght@400;700&family=Tinos:ital,wght@1,700&display=swap">
<style>
  :root {
    --card-light: #fbfbfb;
    --card-mid: #e9e9e9;
    --card-edge: #c9c9c9;
    --brand-red: #d3201f;
    --brand-blue: #2a8ee0;
    --title-blue: #2b6fc9;
    --address-navy: #22308f;
    --ink: #111111;
    --ornament-deep: #6e5866;
    --ornament-soft: #b9adb4;
    --mark-faint: #b5b5b5;
  }
  html, body {
    margin: 0;
    padding: 0;
    width: 1200px;
    height: 686px;
    overflow: hidden;
    background: #ffffff;
  }
  .business-card {
    position: relative;
    width: 1200px;
    height: 686px;
    overflow: hidden;
    background: radial-gradient(ellipse at 45% 55%, var(--card-light) 0%, var(--card-mid) 55%, var(--card-edge) 100%);
    font-family: "PT Sans", "Myriad Pro", Arial, sans-serif;
    color: var(--ink);
  }
  .brand-lockup {
    position: absolute;
    left: 40px;
    top: 34px;
    display: flex;
    align-items: center;
    gap: 26px;
  }
  .brand-square {
    width: 104px;
    height: 104px;
    background: var(--brand-blue);
  }
  .brand-name {
    margin: 0;
    font-weight: 700;
    color: var(--brand-red);
    font-size: 58px;
    line-height: 1.05;
    letter-spacing: 1px;
    text-transform: uppercase;
  }
  .brand-name span { display: block; }
  .brand-name .brand-suffix { font-size: 46px; letter-spacing: 6px; margin-left: 150px; }
  .brand-mark-backdrop {
    position: absolute;
    left: 228px;
    top: 180px;
    width: 410px;
    height: 336px;
    border-radius: 30px;
    background: radial-gradient(ellipse at 50% 50%, rgba(181,181,181,0.45) 0%, rgba(181,181,181,0.18) 60%, rgba(181,181,181,0) 100%);
  }
  .floral-ornament {
    position: absolute;
    right: 0;
    top: 0;
    width: 420px;
    height: 370px;
    background: radial-gradient(ellipse at 62% 42%, var(--ornament-deep) 0%, var(--ornament-soft) 38%, rgba(233,233,233,0) 72%);
    opacity: 0.85;
  }
  .person {
    position: absolute;
    left: 48px;
    top: 262px;
  }
  .person-name {
    margin: 0;
    font-weight: 700;
    font-size: 42px;
    line-height: 1;
  }
  .person-title {
    margin: 12px 0 0 132px;
    font-family: "Tinos", "Times New Roman", serif;
    font-style: italic;
    font-weight: 700;
    font-size: 31px;
    color: var(--title-blue);
  }
  .postal-address {
    position: absolute;
    left: 48px;
    top: 548px;
    font-style: normal;
    font-size: 35px;
    line-height: 46px;
    color: var(--address-navy);
  }
  .contact-list {
    position: absolute;
    left: 667px;
    top: 462px;
    margin: 0;
    padding: 0;
    list-style: none;
    font-size: 29px;
    line-height: 38.5px;
  }
  .contact-list .label { display: inline-block; min-width: 0; margin-right: 10px; }
</style>
</head>
<body>
  <main class="business-card">
    <div class="brand-mark-backdrop" role="img" aria-label="Large faint brand decoration"></div>
    <div class="floral-ornament" role="img" aria-label="Decorative mauve flowers with grey swirling flourishes"></div>

    <header class="brand-lockup">
      <div class="brand-square" aria-hidden="true"></div>
      <h1 class="brand-name"><span>Bright Fern</span><span class="brand-suffix">Co.</span></h1>
    </header>

    <section class="person">
      <p class="person-name">Corisse Pallant</p>
      <p class="person-title">Brand Manager</p>
    </section>

    <address class="postal-address">
      4127 Dunford Avenue<br>
      Burnaby, B.C. V3K 8T2
    </address>

    <ul class="contact-list">
      <li><span class="label">Toll free</span>1-888-519-2063</li>
      <li><span class="label">Phone</span>604-281-7734 ext. 120</li>
      <li><span class="label">Cell</span>604-756-3190</li>
      <li><span class="label">Fax</span>604-281-7739</li>
      <li><span class="label">Email</span>corisse@brightfernco.ca</li>
    </ul>
  </main>
</body>
</html>
```